Stand bag for exclusive, natural snacks

We are looking for a PP stand bag design that will be used to pack exclusive snacks (dried fruits). These snacks will be 100% natural, healthy and without any chemicals. For that reason and for the fact that these products will have a higher price point, the stand bag design should look very premium and happy, while still reminding the customer of the natural, healthy benefits of the snacks inside. The main colors of our brand are black and gold, so we would like to see the packaging in similar colors. In order to be able to see the product, we usually leave some part of the PP packaging transparent.
Packaging Size: h170mm x w80mm x d30mm

Target Market(s)

High-end retail markets with consumers that are willing to pay a little more to get a high-quality product, free from any preservatives and completely natural.

Font styles to use
Sans Serif

Colors

Designer to choose colors to be used in the design.

Requirements
Must have
• - similar to the bag in the sample photos
• - bag size: h170mm x w80mm x d30mm
• - Our logo
• - the colors black & gold
• - Some way of showing the customer the benefit of our dried fruits (healthy, natural, happy)
• - a transparent part to see the product through the plastic foil
Nice to have
• - bottom maybe not transparent in order not to see dust that falls to the bottom

```html
<!DOCTYPE html>
<html lang="en">
<head>
<meta charset="utf-8">
<title>Aurum Pantry – Kiwi, Pomelo and Passion Fruit Stand Bag</title>
<link rel="stylesheet" href="https://fonts.googleapis.com/css2?family=Cinzel:wght@700&family=Nunito:wght@800&family=Oswald:wght@300&display=swap">
<style>
  :root {
    --page: #ffffff;
    --paper: #ffffff;
    --paper-pattern: #efefef;
    --paper-edge: #d9d9d9;
    --ink: #050505;
    --ink-pattern: #1c1c1c;
    --gold: #c7ad6a;
    --gold-light: #efe0b0;
    --gold-dark: #8c7034;
    --fresh-green: #7ab317;
    --leaf-light: #9be05a;
    --leaf-dark: #2f8f1f;
    --mix-brown: #8a4a2c;
    --mix-cream: #e9e1cf;
    --mix-green: #6d9a55;
    --label-white: #ffffff;
  }
  html, body {
    margin: 0;
    width: 1200px;
    height: 1000px;
    overflow: hidden;
    background: var(--page);
  }
  .canvas {
    position: relative;
    width: 1200px;
    height: 1000px;
  }
  .bag-front {
    position: absolute;
    left: 352px;
    top: 35px;
    width: 495px;
    height: 930px;
    display: block;
  }
  .brand-name {
    font-family: "Cinzel", serif;
    font-weight: 700;
    fill: var(--ink);
  }
  .product-title {
    font-family: "Cinzel", serif;
    font-weight: 700;
    fill: var(--fresh-green);
  }
  .claim {
    font-family: "Nunito", sans-serif;
    font-weight: 800;
    fill: var(--label-white);
  }
  .net-weight {
    font-family: "Oswald", sans-serif;
    font-weight: 300;
    fill: var(--label-white);
  }
</style>
</head>
<body>
<main class="canvas">
  <svg class="bag-front" viewBox="0 0 742 1395" xmlns="http://www.w3.org/2000/svg">
    <defs>
      <linearGradient id="gold-trim" x1="0" y1="0" x2="1" y2="0">
        <stop offset="0" stop-color="var(--gold-dark)"/>
        <stop offset="0.45" stop-color="var(--gold-light)"/>
        <stop offset="1" stop-color="var(--gold)"/>
      </linearGradient>
      <linearGradient id="ribbon-gold" x1="0" y1="0" x2="1" y2="0">
        <stop offset="0" stop-color="var(--gold)"/>
        <stop offset="0.5" stop-color="#d2b97a"/>
        <stop offset="1" stop-color="var(--gold)"/>
      </linearGradient>
      <linearGradient id="mix-tones" x1="0" y1="0" x2="1" y2="1">
        <stop offset="0" stop-color="var(--mix-brown)"/>
        <stop offset="0.4" stop-color="var(--mix-cream)"/>
        <stop offset="0.7" stop-color="var(--mix-green)"/>
        <stop offset="1" stop-color="var(--mix-brown)"/>
      </linearGradient>
      <radialGradient id="leaf-tones" cx="0.5" cy="0.45" r="0.6">
        <stop offset="0" stop-color="var(--leaf-light)"/>
        <stop offset="1" stop-color="var(--leaf-dark)"/>
      </radialGradient>
      <radialGradient id="paper-pattern-tone" cx="0.5" cy="0.45" r="0.75">
        <stop offset="0" stop-color="var(--paper)"/>
        <stop offset="1" stop-color="var(--paper-pattern)"/>
      </radialGradient>
      <radialGradient id="ink-pattern-tone" cx="0.5" cy="0.55" r="0.7">
        <stop offset="0" stop-color="var(--ink-pattern)"/>
        <stop offset="1" stop-color="var(--ink)"/>
      </radialGradient>
    </defs>

    <!-- upper panel with botanical line-art area -->
    <rect class="panel-upper" role="img" aria-label="Faint grey botanical line-art pattern of leaves and flowers"
      x="0" y="0" width="742" height="1395" fill="url(#paper-pattern-tone)" stroke="var(--paper-edge)" stroke-width="2"/>

    <!-- gold ribbon -->
    <path class="gold-ribbon" d="M298,0 L440,0 L440,295 L369,272 L298,295 Z" fill="url(#ribbon-gold)"/>

    <!-- brand -->
    <text class="brand-name" x="369" y="172" font-size="46" text-anchor="middle">Aurum Pantry</text>

    <!-- product name -->
    <g class="product-title" font-size="61" text-anchor="middle">
      <text x="373" y="410">KIWI, POMELO AND</text>
      <text x="373" y="478">PASSION FRUIT</text>
      <text x="373" y="545">IN HARMONY</text>
      <text x="373" y="613">WITH PECAN</text>
    </g>

    <!-- lower black panel with nut line-art area -->
    <path class="panel-lower" role="img" aria-label="Dark line-art pattern of nuts and seeds on black"
      d="M0,860 C150,820 300,870 420,960 C520,1030 600,1045 742,1035 L742,1395 L0,1395 Z" fill="url(#ink-pattern-tone)"/>
    <path class="trim-lower" d="M0,860 C150,820 300,870 420,960 C520,1030 600,1045 742,1035" fill="none" stroke="url(#gold-trim)" stroke-width="9"/>

    <!-- product window -->
    <path class="product-window" role="img" aria-label="Window showing the mix of pecans and dried kiwi, pomelo and passion fruit pieces"
      d="M98,800 C200,690 500,640 640,690 C700,720 705,900 685,985 C665,1025 605,1025 560,1005 C450,960 330,860 230,820 C180,800 130,795 98,800 Z"
      fill="url(#mix-tones)" stroke="url(#gold-trim)" stroke-width="9"/>

    <!-- natural leaf -->
    <rect class="leaf-illustration" role="img" aria-label="Fresh green leaf illustration"
      x="305" y="1132" width="140" height="143" rx="60" fill="url(#leaf-tones)"/>

    <text class="claim" x="371" y="1304" font-size="27" text-anchor="middle">100% Natural</text>
    <text class="net-weight" x="371" y="1375" font-size="40" text-anchor="middle">300 G</text>
  </svg>
</main>
</body>
</html>
```